MTSS Pyramid graphic needed for use in presentations and on my website

I am a consultant and need graphics to represent the MTSS pyramid (educational terminology) for use on my website and in slide decks. I've included documentation below that shows the MTSS pyramid, some preferences I have thought of, and my color palette. The MTSS pyramid is well-known in my field and I'd like one that I can use in all my presentations and on my website that looks professional and modern.

Target Market(s)

Educational leaders and educators

Industry/Entity Type

Educational Consulting

Font styles to use
Serif
Sans Serif

Colors
00AB8E
00BBA5
67D7C9
C6EFE9
E9F9F6
6B429C
8869AF
B7A5CE
E3DAEB
F3F0F8

Requirements
Must have
• a pyramid that can be recognized as an MTSS pyramid, use of colors that align with my color palette, a professional, modern look and feel, 3 sections with the largest at the bottom of the pyramid
Nice to have
• rounded corners, maybe 3D
Should not have
• a pyramid in a different shape or orientation, any more or fewer than 3 sections

```html
<!DOCTYPE html>
<html lang="en">
<head>
<meta charset="utf-8">
<title>MTSS Pyramid</title>
<link rel="stylesheet" href="https://fonts.googleapis.com/css2?family=Bebas+Neue&display=swap">
<style>
  :root {
    --bg: #000000;
    --teal-deep: #00AB8E;
    --teal: #00BBA5;
    --teal-light: #67D7C9;
    --teal-pale: #C6EFE9;
    --purple-deep: #6B429C;
    --purple: #8869AF;
    --purple-light: #B7A5CE;
    --tier-intensive: var(--teal-light);
    --tier-intensive-dark: var(--teal);
    --tier-targeted: var(--purple-light);
    --tier-targeted-dark: var(--purple);
    --tier-core: var(--teal);
    --tier-core-dark: var(--teal-deep);
    --label-intensive: var(--teal-light);
    --label-targeted: var(--purple-light);
    --label-core: var(--teal);
  }
  html, body {
    margin: 0;
    padding: 0;
    background: var(--bg);
    overflow: hidden;
  }
  .canvas {
    position: relative;
    width: 1200px;
    height: 543px;
    background: var(--bg);
    overflow: hidden;
  }
  .pyramid {
    position: absolute;
    left: 0;
    top: 0;
    width: 1200px;
    height: 543px;
  }
  .tier-label {
    font-family: "Bebas Neue", "Oswald", sans-serif;
    font-size: 33px;
  }
  .tier-label--intensive { fill: var(--label-intensive); }
  .tier-label--targeted { fill: var(--label-targeted); }
  .tier-label--core { fill: var(--label-core); }
</style>
</head>
<body>
<main class="canvas">
  <svg class="pyramid" viewBox="0 0 1200 543" role="img" aria-label="MTSS pyramid with three tiers: intensive intervention, targeted intervention and core instruction">
    <defs>
      <linearGradient id="grad-core" x1="0" y1="0" x2="1" y2="0">
        <stop offset="0" stop-color="var(--tier-core-dark)"/>
        <stop offset="0.5" stop-color="var(--tier-core)"/>
        <stop offset="1" stop-color="var(--tier-core-dark)"/>
      </linearGradient>
      <linearGradient id="grad-targeted" x1="0" y1="0" x2="1" y2="0">
        <stop offset="0" stop-color="var(--tier-targeted-dark)"/>
        <stop offset="0.5" stop-color="var(--tier-targeted)"/>
        <stop offset="1" stop-color="var(--tier-targeted-dark)"/>
      </linearGradient>
      <linearGradient id="grad-intensive" x1="0" y1="0" x2="1" y2="0">
        <stop offset="0" stop-color="var(--tier-intensive-dark)"/>
        <stop offset="0.5" stop-color="var(--tier-intensive)"/>
        <stop offset="1" stop-color="var(--tier-intensive-dark)"/>
      </linearGradient>
    </defs>

    <g class="tier tier--core">
      <path fill="url(#grad-core)" d="M524 236 Q600 230 676 236 Q690 240 696 252 L757 366 Q764 384 746 386 L456 386 Q437 384 444 366 L505 252 Q511 240 524 236 Z"/>
      <path fill="var(--tier-core-dark)" opacity="0.7" d="M448 374 Q600 392 752 374 L757 380 Q756 388 746 388 L456 388 Q444 388 443 380 Z"/>
    </g>

    <g class="tier tier--targeted">
      <path fill="url(#grad-targeted)" d="M556 168 Q600 165 644 168 Q652 170 655 178 L683 234 Q686 242 676 243 Q600 248 524 243 Q514 242 517 234 L545 178 Q548 170 556 168 Z"/>
      <ellipse cx="600" cy="171" rx="42" ry="3" fill="var(--tier-targeted-dark)" opacity="0.7"/>
    </g>

    <g class="tier tier--intensive">
      <path fill="url(#grad-intensive)" d="M600 116 Q608 116 616 126 L642 157 Q648 164 640 164 Q600 166 560 164 Q552 164 558 157 L584 126 Q592 116 600 116 Z"/>
    </g>

    <text class="tier-label tier-label--intensive" x="677" y="149" textLength="260" lengthAdjust="spacingAndGlyphs">1. Intensive Intervention</text>
    <text class="tier-label tier-label--targeted" x="716" y="206" textLength="259" lengthAdjust="spacingAndGlyphs">2. Targeted Intervention</text>
    <text class="tier-label tier-label--core" x="766" y="269" textLength="198" lengthAdjust="spacingAndGlyphs">3. Core Instruction</text>
  </svg>
</main>
</body>
</html>
```